Halvorn Homes-Real Estate of the Future

Halvorn Homes is a Residential Real Estate company which specializes in buying and selling homes. We pride ourselves on service, expertise, and building relationships. I would like to do a Billboard Ad for a The Size is 14 feet (Height) x 48 feet (width) displaying our current motto for "Real Estate of the Future" We have launched new programs and working with leaders in our industy Brimlot and other tech companies and changing the way Real Estate is done in Las Vegas, NV. Its exciting and NEW so we want to get the word out. Color Scheme Red, White, Grey and maybe black. Logo is uploaded and so is a picture head shot. I would like to see options with my headshot and with out.

```html
<!DOCTYPE html>
<html lang="en">
<head>
<meta charset="utf-8">
<title>Halvorn Homes – Real Estate of the Future Billboard</title>
<link href="https://fonts.googleapis.com/css2?family=Oswald:wght@200;500;700&display=swap" rel="stylesheet">
<style>
  :root {
    --page-bg: #e9ebee;
    --board-white: #ffffff;
    --brand-red: #c0202a;
    --band-grey: #3c3d40;
    --text-white: #ffffff;
    --photo-sky: #9fbfdc;
    --photo-stucco: #d9cfc2;
    --photo-green: #7c9160;
    --portrait-light: #f2f2f2;
    --portrait-navy: #1d2740;
  }
  * { margin: 0; padding: 0; box-sizing: border-box; }
  html, body {
    width: 1200px;
    height: 900px;
    overflow: hidden;
    background: var(--page-bg);
  }
  .canvas {
    width: 1200px;
    height: 900px;
    display: flex;
    align-items: center;
    justify-content: center;
  }
  .billboard {
    width: 1160px;
    height: 338px;
    display: block;
    box-shadow: 0 6px 24px rgba(0,0,0,0.18);
  }
  .brand-name {
    font-family: "Oswald", sans-serif;
    font-weight: 500;
    fill: var(--brand-red);
  }
  .tagline-lead {
    font-family: "Oswald", sans-serif;
    font-weight: 700;
    fill: var(--text-white);
  }
  .tagline-key {
    font-family: "Oswald", sans-serif;
    font-weight: 200;
    fill: var(--text-white);
  }
</style>
</head>
<body>
<main class="canvas">
  <svg class="billboard" viewBox="0 0 1160 338" xmlns="http://www.w3.org/2000/svg" aria-label="Halvorn Homes billboard: Real Estate of the Future">
    <defs>
      <linearGradient id="homePhotoTones" x1="0" y1="0" x2="0" y2="1">
        <stop offset="0" stop-color="var(--photo-sky)"/>
        <stop offset="0.25" stop-color="var(--photo-green)"/>
        <stop offset="0.45" stop-color="var(--photo-stucco)"/>
        <stop offset="0.8" stop-color="var(--photo-stucco)"/>
        <stop offset="1" stop-color="var(--photo-green)"/>
      </linearGradient>
      <linearGradient id="portraitTones" x1="0" y1="0" x2="0" y2="1">
        <stop offset="0" stop-color="var(--portrait-light)"/>
        <stop offset="0.55" stop-color="#c8b8a8"/>
        <stop offset="0.62" stop-color="var(--portrait-navy)"/>
        <stop offset="1" stop-color="var(--portrait-navy)"/>
      </linearGradient>
    </defs>

    <rect class="board-base" x="0" y="0" width="1160" height="338" fill="var(--board-white)"/>

    <polygon class="tagline-band" points="514,115 900,115 900,300 419,300 555,150" fill="var(--band-grey)"/>

    <polygon class="home-photo" role="img" aria-label="Photo of a single-storey stucco home with landscaped front yard and hillside homes behind"
             points="0,0 380,0 540,150 370,338 0,338" fill="url(#homePhotoTones)"/>

    <polyline class="chevron-stripe" points="382,-2 548,150 372,340" fill="none" stroke="var(--brand-red)" stroke-width="10" stroke-linejoin="miter"/>

    <g class="brand-lockup">
      <rect x="586" y="44" width="34" height="34" fill="var(--brand-red)"/>
      <text class="brand-name" x="634" y="78" font-size="44">Halvorn Homes</text>
    </g>

    <text class="tagline-lead" x="588" y="176" font-size="42" textLength="302" lengthAdjust="spacingAndGlyphs">Real Estate of the</text>
    <text class="tagline-key" x="584" y="282" font-size="108" textLength="306" lengthAdjust="spacingAndGlyphs">FUTURE</text>

    <rect class="agent-portrait" role="img" aria-label="Headshot of the agent in a navy blazer and blue shirt"
          x="900" y="12" width="246" height="310" fill="url(#portraitTones)"/>
  </svg>
</main>
</body>
</html>
```